Simplified Double Diamond Diagram for Book

I need a simplified version of the Double Diamond Diagram for a book I am working on. I would like to represent the diagram with the following image/text:
- Two diamonds connected (as in each of the sample photos)
- Inclusion of "Diverge" "Converge" above each of the sides of the diamonds as shown in sample image 1 - without elaborative text
- Inclusion of "Problem" and "Solution" in each diamond as is shown in the example image 2
- I need a color version and black/white version of the image that can be turned into a mono-color version in the book.

```html
<!DOCTYPE html>
<html lang="en">
<head>
<meta charset="utf-8">
<title>Double Diamond — Diverge and Converge</title>
<link rel="stylesheet" href="https://fonts.googleapis.com/css2?family=Montserrat:wght@400;700&display=swap">
<style>
  :root {
    --paper: #ffffff;
    --outline: #6a6a66;
    --problem-diverge: #8a8984;
    --problem-converge: #b6b5b0;
    --solution-diverge: #bdbdbd;
    --solution-converge: #767676;
    --phase-ink: #000000;
    --problem-ink: #5e5d59;
    --solution-ink: #7c7c7c;
  }
  html, body {
    margin: 0;
    padding: 0;
    width: 1200px;
    height: 676px;
    overflow: hidden;
    background: var(--paper);
  }
  .double-diamond {
    display: block;
    width: 1200px;
    height: 676px;
  }
  .half--problem-diverge { fill: var(--problem-diverge); }
  .half--problem-converge { fill: var(--problem-converge); }
  .half--solution-diverge { fill: var(--solution-diverge); }
  .half--solution-converge { fill: var(--solution-converge); }
  .diamond-outline,
  .lead-line {
    fill: none;
    stroke: var(--outline);
    stroke-width: 10;
    stroke-linejoin: miter;
  }
  .phase-label {
    font-family: "Montserrat", sans-serif;
    font-weight: 700;
    font-size: 50px;
    letter-spacing: 1px;
    fill: var(--phase-ink);
    text-anchor: middle;
  }
  .stage-label {
    font-family: "Montserrat", sans-serif;
    font-weight: 400;
    font-size: 46px;
    letter-spacing: 2px;
    text-anchor: middle;
    dominant-baseline: central;
  }
  .stage-label--problem { fill: var(--problem-ink); }
  .stage-label--solution { fill: var(--solution-ink); }
</style>
</head>
<body>
<svg class="double-diamond" viewBox="0 0 1770 997" xmlns="http://www.w3.org/2000/svg" role="img" aria-label="Double diamond diagram: diverge and converge on the problem, then diverge and converge on the solution">
  <!-- Problem diamond -->
  <g class="diamond diamond--problem">
    <polygon class="half--problem-diverge" points="517,130 517,866 150,497"/>
    <polygon class="half--problem-converge" points="517,130 884,497 517,866"/>
    <polygon class="diamond-outline" points="517,130 884,497 517,866 150,497"/>
    <text class="stage-label stage-label--problem" x="517" y="497">PROBLEM</text>
  </g>

  <!-- Solution diamond -->
  <g class="diamond diamond--solution">
    <polygon class="half--solution-diverge" points="1251,130 1251,866 884,497"/>
    <polygon class="half--solution-converge" points="1251,130 1618,497 1251,866"/>
    <polygon class="diamond-outline" points="1251,130 1618,497 1251,866 884,497"/>
    <text class="stage-label stage-label--solution" x="1247" y="497">SOLUTION</text>
  </g>

  <!-- Entry and exit lines -->
  <g class="lead-lines">
    <line class="lead-line" x1="91" y1="438" x2="150" y2="497"/>
    <line class="lead-line" x1="91" y1="558" x2="150" y2="497"/>
    <line class="lead-line" x1="1680" y1="438" x2="1618" y2="497"/>
    <line class="lead-line" x1="1680" y1="558" x2="1618" y2="497"/>
  </g>

  <!-- Phase labels -->
  <g class="phase-labels">
    <text class="phase-label" transform="translate(310 292) rotate(-45)">DIVERGE</text>
    <text class="phase-label" transform="translate(722 296) rotate(45)">CONVERGE</text>
    <text class="phase-label" transform="translate(1044 292) rotate(-45)">DIVERGE</text>
    <text class="phase-label" transform="translate(1456 296) rotate(45)">CONVERGE</text>
  </g>
</svg>
</body>
</html>
```